Positive Psychology and Coaching Web Design Project

I am a trained psychologist and need to develop a website for my positive life coaching and positive psychology training business. My business is based on Positive Psychology, which is the science of human performance enhancement, to help people reach their potential and flourish in their lives. I work with both individuals, and groups in both businesses and schools helping people improve and create more positive, authentic and successful lives by enhancing their performance and improving their wellbeing, resilience, happiness and quality of life.
The business name: My company is named after a fruit, the pomegranate, which is a very special super fruit, with health enhancing benefits and it is a symbol for growth and positive relationships. The pomegranate is full of many seeds, which represent potential, possibilities and ideas.
The website should have integrity, be professional, strong, inspiring and authentic.

Target Market(s)

I coach and work with executives, individuals and children one-on-one, and also teach and train groups in both businesses and schools. The website needs to be professional, in order to fit into the corporate world of executive coaching, but also friendly and inspiring to fit in with positive education in schools.

Industry/Entity Type

Life Coaching

Font styles to use
Sans Serif

Requirements
Must have
• Use of my logo, however, it is flexible how it is used, and the designer can choose which version to use. There is a closed pomegranate with leaves, an open pomegranate to show seeds with leaves, and both of these without leaves.
See attached files:
File 1: A.png: preferred version used on back of business card
File 4: B.png: preferred version but not used anywhere yet, but goes nicely with A?
File 3: C.png: open pomegranate with seeds used on text side of business card
File 2: D.png: plain pomegranate, could be used as a bullet point??!

A home page with toggle buttons to go to other pages such as:
Home
About
Individuals & Organisations
Young People & Schools
Resources
Contact
Nice to have
• The pomegranate is full of many seeds, which represent potential, possibilities and ideas. My logo has a version with the closed pomegranate, and one with the open pomegranate revealing the seeds. Both these could be used on the website, perhaps clicking on the closed pomegranate to reveal the seeds??! My business card has the closed pomegranate on the back and the open seed pomegranate on the side with my name and details. I trust the designer to choose professional suitable colours, however, I do like the colours used on my logo and business card and the consistency might be nice, these colours are:
Pomegranate Red Colour C:24.67%, M: 100%, Y: 100%, K: 24.49%;
Green Writing Colour: C: 71.16%, M: 49.66%, Y: 100%, K: 54.04%
Green Leaf Colour: C: 69.18%, M: 47.02%, Y: 100%, K: 48.21%

```html
<!DOCTYPE html>
<html lang="en">
<head>
<meta charset="utf-8">
<title>Brightfield Consulting – Positive Psychology &amp; Life Coaching</title>
<link href="https://fonts.googleapis.com/css2?family=Outfit:wght@500;600&family=Questrial&display=swap" rel="stylesheet">
<style>
  :root {
    --red: #9b1205;
    --red-dark: #5a1510;
    --ink: #111111;
    --charcoal: #2a2a2a;
    --black: #050505;
    --text: #3c3c3c;
    --muted: #777777;
    --rule: #e6e6e6;
    --white: #ffffff;
    --footer-note: #c9706a;
  }
  * { box-sizing: border-box; margin: 0; padding: 0; }
  html, body { width: 1036px; height: 1200px; overflow: hidden; }
  body {
    background: var(--white);
    font-family: "Questrial", "Century Gothic", sans-serif;
    color: var(--text);
    border-top: 3px solid var(--red);
  }
  .heading { font-family: "Outfit", "Century Gothic", sans-serif; font-weight: 600; }

  /* Header */
  .site-header { height: 134px; position: relative; }
  .brand {
    position: absolute; left: 80px; top: 48px;
    font-size: 30px; color: var(--red); letter-spacing: -0.3px;
  }
  .contact-block {
    position: absolute; right: 70px; top: 32px; width: 184px;
    text-align: right; font-family: "Outfit", sans-serif; font-weight: 600;
    font-size: 13px; color: #444; line-height: 19px;
  }
  .contact-block .email { border-top: 1px solid #ddd; margin-top: 5px; padding-top: 6px; }

  /* Navigation */
  .main-nav { background: var(--red); height: 52px; padding-left: 60px; display: flex; }
  .main-nav a {
    color: var(--white); text-decoration: none; font-family: "Outfit", sans-serif;
    font-weight: 600; font-size: 16px; line-height: 52px; padding: 0 20px;
  }
  .main-nav a.active { background: var(--black); }

  /* Hero */
  .hero { background: var(--charcoal); height: 287px; text-align: center; color: var(--white); padding-top: 58px; }
  .hero h1 { font-size: 35px; letter-spacing: 0.3px; }
  .hero p { font-size: 16.5px; line-height: 23px; width: 580px; margin: 14px auto 0; }
  .hero .btn-outline {
    display: inline-block; margin-top: 22px; width: 158px; height: 40px; line-height: 38px;
    border: 1px solid #9a9a9a; color: var(--white); font-size: 16px; text-decoration: none;
  }

  /* Program band */
  .programs { background: var(--red); height: 225px; position: relative; color: var(--white); }
  .program { position: absolute; top: 40px; width: 270px; }
  .program h2 { font-size: 17.5px; line-height: 21px; }
  .program p { font-size: 13.5px; line-height: 18px; margin-top: 16px; }
  .program .btn {
    display: inline-block; margin-top: 22px; background: var(--red-dark); color: var(--white);
    font-family: "Outfit", sans-serif; font-weight: 600; font-size: 13px; text-decoration: none;
    padding: 0 16px; height: 30px; line-height: 30px; border-radius: 5px;
  }
  .program.p1 { left: 60px; }
  .program.p2 { left: 376px; }
  .program.p3 { left: 690px; }
  .program.p3 p { margin-top: 10px; }
  .program.p3 .btn { margin-top: 16px; }

  /* Main content */
  .content { position: relative; height: 382px; }
  .intro { position: absolute; left: 60px; top: 50px; width: 605px; }
  .intro h2, .news h2 { font-size: 22px; color: var(--ink); }
  .intro .lead { font-size: 16.5px; line-height: 22px; margin-top: 16px; }
  .intro .body { font-size: 16.5px; line-height: 22px; margin-top: 12px; }
  .text-link { color: var(--red); font-size: 16.5px; text-decoration: underline; display: inline-block; margin-top: 12px; }
  .news-divider { position: absolute; left: 676px; top: 59px; width: 7px; height: 259px; background: var(--rule); }
  .news { position: absolute; left: 706px; top: 50px; width: 265px; }
  .news .date { font-size: 13.5px; color: var(--muted); margin-top: 12px; }
  .news .excerpt { font-size: 16.5px; line-height: 22px; margin-top: 10px; }
  .news .text-link { margin-top: 14px; margin-left: 2px; }

  /* Footer */
  .site-footer { background: var(--red); height: 121px; text-align: center; padding-top: 30px; }
  .footer-nav { font-size: 14px; color: var(--white); }
  .footer-nav a { color: var(--white); text-decoration: none; }
  .footer-nav .sep { margin: 0 20px; }
  .footer-note { margin-top: 16px; font-size: 13.5px; color: var(--footer-note); }
</style>
</head>
<body>
  <header class="site-header">
    <div class="brand">Brightfield Consulting</div>
    <div class="contact-block">
      <div>Call us:</div>
      <div>1800-555-019</div>
      <div class="email">info@brightfield.com.au</div>
    </div>
  </header>

  <nav class="main-nav">
    <a href="#" class="active">Home</a>
    <a href="#">About</a>
    <a href="#">Individuals &amp; Organisations</a>
    <a href="#">Young People &amp; Schools</a>
    <a href="#">Resources</a>
    <a href="#">Contact</a>
  </nav>

  <section class="hero">
    <h1 class="heading">Positive Psychology &amp; Life Coaching</h1>
    <p>Lorem ipsum dolor sit amet, consectetur adipiscing elit. Donec est leo, viverra eget risus ac, euismod elementum odio.</p>
    <a href="#" class="btn-outline">Lorem ipsum</a>
  </section>

  <section class="programs">
    <div class="program p1">
      <h2 class="heading">Programs for Individuals and Organisations</h2>
      <p>Lorem ipsum dolor sit amet, consectetur adipiscing elit. Nulla sed ipsum pulvinar.</p>
      <a href="#" class="btn">Lorem ipsum</a>
    </div>
    <div class="program p2">
      <h2 class="heading">Programs for Young People and Schools</h2>
      <p>Lorem ipsum dolor sit amet, consectetur adipiscing elit. Nulla sed ipsum pulvinar.</p>
      <a href="#" class="btn">Lorem ipsum</a>
    </div>
    <div class="program p3">
      <h2 class="heading">Other Programs and Resources</h2>
      <p>Lorem ipsum dolor sit amet, consectetur adipiscing elit. Nulla sed ipsum pulvinar.</p>
      <a href="#" class="btn">Lorem ipsum</a>
    </div>
  </section>

  <main class="content">
    <article class="intro">
      <h2 class="heading">Positive Psychology &amp; Life Coaching</h2>
      <p class="lead">The science of human performance enhancement, to help people reach their potential and flourish in their lives.</p>
      <p class="body">I work with both individuals, and groups in both businesses and schools helping people improve and create more positive, authentic and successful lives by enhancing their performance and improving their wellbeing, resilience, happiness and quality of life.</p>
      <a href="#" class="text-link">Learn more about our approach</a>
    </article>
    <div class="news-divider"></div>
    <aside class="news">
      <h2 class="heading">Latest News</h2>
      <p class="date">Posted on: 2 Jun, 2015</p>
      <p class="excerpt">Nullam fringilla enim eget sem ultricies, et aliquam libero lacinia. Praesent tortor erat, pharetra quis tellus id, scelerisque dapibus dui. [...]</p>
      <a href="#" class="text-link">Read more</a>
    </aside>
  </main>

  <footer class="site-footer">
    <div class="footer-nav">
      <a href="#">Home</a><span class="sep">|</span>
      <a href="#">About</a><span class="sep">|</span>
      <a href="#">Individuals &amp; Organisations</a><span class="sep">|</span>
      <a href="#">Young People &amp; Schools</a><span class="sep">|</span>
      <a href="#">Resources</a><span class="sep">|</span>
      <a href="#">Contact</a>
    </div>
    <p class="footer-note">Lorem ipsum dolor sit amet, consectetur adipiscing elit.</p>
  </footer>
</body>
</html>
```